Branding website for a Data Science company with 1 product

Branding website for a Data Science company, featuring our main product: Lumoria. The purpose of the website is to get potential clients to get a peek at what we do, but the main purpose is to get them to get in touch with us. The website will not answer all questions. Therefore the contact details and contact form is a must-have .

Target Market(s)

Potential new B2B clients with medium to large websites, application users (behind a login)

Industry/Entity Type

It Company

Coding

Coded - Design and coding required

Number of Pages Required

2 page

Font styles to use
Sans Serif

Colors

Designer to choose colors to be used in the design.

Requirements
Must have
• A contact form and branding a product

```html
<!DOCTYPE html>
<html lang="en">
<head>
<meta charset="utf-8">
<title>Quantile Partners — Data Science Company</title>
<link href="https://fonts.googleapis.com/css2?family=Open+Sans:wght@300;400;600;700&display=swap" rel="stylesheet">
<style>
  :root {
    --hero-bg: #3a3a3b;
    --hero-deep: #2c2c2e;
    --accent: #e0562a;
    --text-light: #e6e6e6;
    --text-muted: #9a9a9a;
    --text-ghost: #575758;
    --page-white: #ffffff;
  }
  * { margin: 0; padding: 0; box-sizing: border-box; }
  html, body {
    width: 1200px; height: 938px; overflow: hidden;
    background: var(--page-white);
    font-family: "Open Sans", Arial, sans-serif;
  }
  .page { position: relative; width: 1200px; height: 938px; }
  .hero {
    position: absolute; left: 0; top: 0; width: 1200px; height: 680px;
    background: linear-gradient(180deg, var(--hero-deep) 0%, var(--hero-bg) 100%);
    overflow: hidden;
  }
  .hero-visual { position: absolute; left: 0; top: 0; width: 1200px; height: 680px; }
  .brand {
    position: absolute; left: 22px; top: 34px;
    display: flex; align-items: center; gap: 10px;
    color: var(--accent); font-weight: 400; font-size: 26px; letter-spacing: 1px;
  }
  .brand-dot { width: 16px; height: 16px; border-radius: 50%; background: var(--accent); }
  .menu-toggle { position: absolute; left: 1132px; top: 34px; width: 30px; }
  .menu-toggle span { display: block; height: 3px; background: var(--text-light); margin-bottom: 6px; }
  .section-index {
    position: absolute; left: 25px; top: 172px;
    color: var(--text-light); font-size: 34px; font-weight: 600; letter-spacing: 3px;
  }
  .section-nav { position: absolute; left: 0; top: 0; }
  .nav-dot { position: absolute; width: 8px; height: 8px; border-radius: 50%; background: var(--text-muted); }
  .nav-dot.active { background: var(--text-light); width: 10px; height: 10px; }
  .nav-line { position: absolute; left: 46px; top: 276px; width: 2px; height: 64px; background: var(--text-light); }
  .nav-label {
    position: absolute; left: 70px; top: 244px;
    color: var(--text-light); font-size: 9px; font-weight: 700; letter-spacing: 1px;
  }
  .tagline {
    position: absolute; left: 338px; top: 322px;
    color: var(--text-light); font-size: 20px; font-weight: 600; letter-spacing: 6px;
  }
  .tagline-rule { position: absolute; left: 338px; top: 377px; width: 146px; height: 2px; background: var(--accent); }
  .read-more {
    position: absolute; left: 338px; top: 396px;
    color: var(--text-light); font-size: 9px; font-weight: 700; letter-spacing: 1px;
    display: flex; align-items: center; gap: 6px; text-decoration: none;
  }
  .read-more i { display: block; width: 14px; height: 2px; background: var(--accent); }
  .ghost-word {
    position: absolute; left: 20px; top: 566px;
    color: var(--text-ghost); font-size: 62px; font-weight: 700; letter-spacing: 44px;
  }
  .scroll-cue { position: absolute; left: 393px; top: 506px; }
  .scroll-line { position: absolute; left: 401px; top: 540px; width: 2px; height: 140px; background: var(--text-muted); }
  .scroll-label {
    position: absolute; left: 417px; top: 540px;
    writing-mode: vertical-rl; color: var(--text-muted);
    font-size: 8px; letter-spacing: 1px; font-weight: 600;
  }
</style>
</head>
<body>
<div class="page">
  <section class="hero">
    <svg class="hero-visual" viewBox="0 0 1200 680" role="img" aria-label="Photograph of a planet seen from space with a bright light sweep">
      <defs>
        <radialGradient id="planetGlow" cx="0.45" cy="0.45" r="0.6">
          <stop offset="0" stop-color="#2f3a3e"/>
          <stop offset="0.7" stop-color="#263035"/>
          <stop offset="1" stop-color="#1f2427"/>
        </radialGradient>
        <linearGradient id="lightSweep" x1="0" y1="0" x2="1" y2="0">
          <stop offset="0" stop-color="#6a6a6a" stop-opacity="0.55"/>
          <stop offset="1" stop-color="#4a4a4b" stop-opacity="0.2"/>
        </linearGradient>
      </defs>
      <circle cx="780" cy="380" r="470" fill="url(#planetGlow)" opacity="0.75"/>
      <path d="M1060 0 H1200 V680 H1260 C1210 420 1170 200 1060 0 Z" fill="url(#lightSweep)"/>
      <path d="M1060 0 C1160 180 1200 420 1200 680 V680 H1200 V0 Z" fill="none"/>
      <path d="M1040 0 C1130 200 1170 440 1150 680 H1200 V0 Z" fill="url(#lightSweep)"/>
    </svg>

    <div class="brand"><span class="brand-dot"></span><span>QUANTILE PARTNERS</span></div>
    <div class="menu-toggle" aria-label="Menu"><span></span><span></span><span></span></div>

    <div class="section-index">01</div>
    <nav class="section-nav" aria-label="Sections">
      <span class="nav-dot active" style="left:42px;top:246px"></span>
      <span class="nav-label">HOME</span>
      <span class="nav-line"></span>
      <span class="nav-dot" style="left:43px;top:358px"></span>
      <span class="nav-dot" style="left:43px;top:388px"></span>
      <span class="nav-dot" style="left:43px;top:418px"></span>
      <span class="nav-dot" style="left:43px;top:446px"></span>
    </nav>

    <h1 class="tagline">DATA SCIENCE COMPANY</h1>
    <span class="tagline-rule"></span>
    <a class="read-more" href="#about">READ MORE <i></i></a>

    <div class="ghost-word">DATA</div>

    <svg class="scroll-cue" width="18" height="30" viewBox="0 0 18 30" aria-hidden="true">
      <rect x="2" y="2" width="14" height="24" rx="7" fill="none" stroke="#b5b5b5" stroke-width="2"/>
      <line x1="9" y1="7" x2="9" y2="12" stroke="#b5b5b5" stroke-width="2"/>
    </svg>
    <span class="scroll-line"></span>
    <span class="scroll-label">SCROLL DOWN</span>
  </section>
</div>
</body>
</html>
```